Business card design for Velluto Events, and Event & Entertainment business

The business card design is for a new business venture, Velluto Events. This company offers Event management, entertainment management and also Latin dance tuition. We currently run Latin dance festivals in Australia & also teach street Latin. This business card is for the director, Mara Dunhill. The Logo has already been designed. So, I need the new design to incorporate and go with the existing Logo.

The look I like is clean, simple & elegant but I also want it to be sexy. Elegant, but not corporate. Clean & simple but not boring :-)

If you want to add another design element as well as using the Logo, please use something with movement. I like ripples or swirls for example.

I would also like to have part of the card embossed or Spot UV pressed so I would like some part of the design to have texture.

Text for the Cards is as follows;

Velluto Events ( Logo attached )

Mara Dunhill

EVENTS & ENTERTAINMENT MANAGEMENT

m: 0478 352 601
e: mara@vellutoevents.com.au
f Velluto Events

www.vellutoevents.com.au

Please try portrait layout.

Thanks, Mara
Updates

Hello Designers, Thank you to all of you who have submitted designs for Velluto Events. I will make up my mind now from what I have already been sent. Very close to making a decision :-) Thank you, Mara

Target Market(s)

Adults, 18 - 60 age group. People who are active. People interested in different cultures. People who like to travel. Please who like to have fun. People who are passionate about Latin dance.

Industry/Entity Type

Entertainment

Font styles to use
Sans Serif
Script

Colors
9bcb3c
ec1f27
ffffff

Requirements
Must have
• Logo + All text listed in brief
Nice to have
• An extra design feature or background image that could be embossed or spot uv pressed to add texture & flare.

```html
<!DOCTYPE html>
<html lang="en">
<head>
<meta charset="utf-8">
<title>Velluto Events – Business Card</title>
<link rel="stylesheet" href="https://fonts.googleapis.com/css2?family=Mulish:wght@400;700&display=swap">
<style>
  :root {
    --page: #dcd9d4;
    --card: #f5f2ed;
    --ink: #2f2f2f;
    --ink-soft: #4a4a4a;
    --red: #ec1f27;
    --green: #9bcb3c;
    --emboss: #e4e0d8;
    --divider: #3a3a3a;
  }
  * { box-sizing: border-box; margin: 0; padding: 0; }
  html, body { width: 1062px; height: 1200px; overflow: hidden; }
  body {
    background: var(--page);
    font-family: "Mulish", sans-serif;
    color: var(--ink);
    display: flex;
    flex-direction: column;
    align-items: center;
    justify-content: center;
    gap: 56px;
  }
  .card {
    position: relative;
    width: 880px;
    height: 536px;
    background: var(--card);
    overflow: hidden;
  }

  /* Front */
  .card-front__accent {
    position: absolute;
    right: -70px;
    top: -40px;
    width: 300px;
    height: 300px;
    border-radius: 50%;
    background: radial-gradient(circle, rgba(236,31,39,0.10), rgba(155,203,60,0.08) 70%, rgba(155,203,60,0) 100%);
  }
  .brand {
    position: absolute;
    left: 70px;
    top: 200px;
    width: 240px;
    display: flex;
    align-items: center;
    gap: 14px;
  }
  .brand__dot {
    flex: none;
    width: 22px;
    height: 22px;
    border-radius: 50%;
    background: var(--red);
  }
  .brand__name {
    font-size: 38px;
    font-weight: 400;
    line-height: 1.1;
    color: var(--ink);
  }
  .divider {
    position: absolute;
    left: 330px;
    top: 160px;
    width: 2px;
    height: 178px;
    background: var(--divider);
  }
  .contact {
    position: absolute;
    left: 358px;
    top: 158px;
  }
  .contact__name {
    font-size: 23px;
    font-weight: 700;
    letter-spacing: 0.5px;
    text-transform: uppercase;
    color: var(--ink);
    margin-bottom: 20px;
  }
  .contact__list { list-style: none; }
  .contact__item {
    display: flex;
    align-items: center;
    gap: 10px;
    font-size: 17px;
    line-height: 27px;
    color: var(--ink-soft);
  }
  .contact__icon { width: 14px; height: 14px; flex: none; }
  .contact__icon--square { background: var(--red); width: 11px; height: 11px; margin: 0 1.5px; }
  .contact__web {
    margin-top: 26px;
    font-size: 17px;
    font-weight: 700;
    color: var(--ink);
  }
  .tagline {
    position: absolute;
    left: 0;
    right: 0;
    top: 418px;
    text-align: center;
    font-size: 18px;
    letter-spacing: 2px;
    text-transform: uppercase;
    color: var(--ink-soft);
  }

  /* Back */
  .card-back {
    display: flex;
    align-items: center;
    justify-content: center;
  }
  .emboss-mark {
    display: flex;
    align-items: center;
    gap: 22px;
  }
  .emboss-mark__dot {
    width: 34px;
    height: 34px;
    border-radius: 50%;
    background: var(--emboss);
  }
  .emboss-mark__name {
    font-size: 64px;
    font-weight: 400;
    color: var(--emboss);
  }
</style>
</head>
<body>

  <section class="card card-front" aria-label="Business card front">
    <div class="card-front__accent"></div>

    <div class="brand">
      <span class="brand__dot"></span>
      <span class="brand__name">Velluto Events</span>
    </div>

    <div class="divider"></div>

    <div class="contact">
      <h1 class="contact__name">Mara Dunhill</h1>
      <ul class="contact__list">
        <li class="contact__item">
          <svg class="contact__icon" viewBox="0 0 14 14" aria-hidden="true">
            <path d="M1 4 Q7 0 13 4 L11 6 L9 4.5 L5 4.5 L3 6 Z" fill="var(--red)"/>
            <rect x="3" y="7" width="8" height="6" rx="1" fill="var(--red)"/>
          </svg>
          0478 352 601
        </li>
        <li class="contact__item">
          <svg class="contact__icon" viewBox="0 0 14 14" aria-hidden="true">
            <rect x="1" y="3" width="12" height="8" fill="var(--red)"/>
            <path d="M1 3 L7 8 L13 3" fill="none" stroke="var(--card)" stroke-width="1.2"/>
          </svg>
          mara@vellutoevents.com.au
        </li>
        <li class="contact__item">
          <span class="contact__icon contact__icon--square"></span>
          Velluto Events
        </li>
      </ul>
      <p class="contact__web">www.vellutoevents.com.au</p>
    </div>

    <p class="tagline">Events &amp; Entertainment Management</p>
  </section>

  <section class="card card-back" aria-label="Business card back, embossed">
    <div class="emboss-mark">
      <span class="emboss-mark__dot"></span>
      <span class="emboss-mark__name">Velluto Events</span>
    </div>
  </section>

</body>
</html>
```